Harbor Ridge Seed Collective business cards

Create a single-sided business card for the Harbor Ridge Seed Collective based on the attached logo.
The additional data fields include Name, Title, Email, Phone, and website.
Please use the following as sample data:
Name: Dana Vellor
Title: Co-Founder / Investor
Email: danavellor@mailbrook.example
Phone: 805-555-0147
Website: www.hrseedcollective.example

Target Market(s)

Start ups, entrepreneurs, venture capitalists

Industry/Entity Type

Investment

Contact Information for Business Card

Professional business card. Technology company.

Font styles to use
Serif
Sans Serif

Requirements
Must have
• Include the HRSC logo (attached)
• Name
• Title
• Email
• Phone
• Website
Should not have
• Cute, cartoony

```html
<!DOCTYPE html>
<html lang="en">
<head>
<meta charset="utf-8">
<title>Harbor Ridge Seed Collective — Business Card</title>
<link rel="stylesheet" href="https://fonts.googleapis.com/css2?family=Roboto+Condensed:wght@400;700&family=Source+Sans+3:wght@400&display=swap">
<style>
  :root {
    --brand-green: #267a43;
    --ink-dark: #30373a;
    --paper: #f4f5f5;
    --backdrop: #e3e6e7;
    --white: #ffffff;
    --band-light: #e9eeec;
  }
  html, body {
    margin: 0;
    width: 1200px;
    height: 900px;
    overflow: hidden;
    background: var(--backdrop);
  }
  .canvas {
    position: relative;
    width: 1200px;
    height: 900px;
  }
  .business-card {
    position: absolute;
    left: 75px;
    top: 150px;
    width: 1050px;
    height: 600px;
    background: var(--paper);
    box-shadow: 0 6px 24px rgba(0,0,0,0.12);
    overflow: hidden;
  }
  .card-art {
    position: absolute;
    inset: 0;
    width: 1050px;
    height: 600px;
  }
  .brand-lockup {
    position: absolute;
    left: 56px;
    top: 94px;
    height: 158px;
    display: flex;
    align-items: center;
  }
  .brand-mark {
    width: 92px;
    height: 92px;
    border-radius: 50%;
    background: var(--brand-green);
    margin-right: 30px;
  }
  .brand-divider {
    width: 2px;
    height: 158px;
    background: var(--brand-green);
    margin-right: 22px;
  }
  .brand-name {
    font-family: "Source Sans 3", sans-serif;
    font-weight: 400;
    color: var(--brand-green);
    font-size: 44px;
    line-height: 1.05;
    margin: 0;
  }
  .contact-block {
    position: absolute;
    left: 62px;
    top: 0;
    font-family: "Roboto Condensed", sans-serif;
    color: var(--ink-dark);
  }
  .person-name {
    position: absolute;
    top: 352px;
    margin: 0;
    font-size: 41px;
    font-weight: 700;
    white-space: nowrap;
    line-height: 1;
  }
  .person-name .family-name { color: var(--white); }
  .person-title {
    position: absolute;
    top: 405px;
    margin: 0;
    font-size: 31px;
    font-weight: 400;
    white-space: nowrap;
    line-height: 1;
  }
  .contact-line {
    position: absolute;
    margin: 0;
    font-size: 28px;
    font-weight: 400;
    white-space: nowrap;
    line-height: 1;
  }
  .contact-email { top: 460px; }
  .contact-phone { top: 494px; }
  .contact-web { top: 526px; }
</style>
</head>
<body>
<main class="canvas">
  <article class="business-card">
    <svg class="card-art" viewBox="0 0 750 428" preserveAspectRatio="none" aria-hidden="false">
      <defs>
        <linearGradient id="pattern-tone" x1="0" y1="0" x2="1" y2="1">
          <stop offset="0" stop-color="#dfe6e2"/>
          <stop offset="0.5" stop-color="#c9d6cd"/>
          <stop offset="1" stop-color="#d9e0dc"/>
        </linearGradient>
      </defs>
      <rect class="top-panel" x="0" y="0" width="750" height="214" fill="var(--paper)"/>
      <polygon class="contact-panel" points="0,214 447,214 660,428 0,428" fill="var(--brand-green)"/>
      <polygon class="accent-band-light" points="447,214 482,214 692,428 660,428" fill="var(--band-light)"/>
      <polygon class="accent-band-green" points="447,214 660,0 692,0 480,214" fill="var(--brand-green)"/>
      <polygon class="dot-field" role="img" aria-label="Decorative field of green and charcoal dots" points="480,214 692,0 750,0 750,428 692,428" fill="url(#pattern-tone)"/>
    </svg>

    <div class="brand-lockup">
      <span class="brand-mark" aria-hidden="true"></span>
      <span class="brand-divider" aria-hidden="true"></span>
      <h1 class="brand-name">Harbor Ridge<br>Seed Collective</h1>
    </div>

    <div class="contact-block">
      <h2 class="person-name">DANA <span class="family-name">VELLOR</span></h2>
      <p class="person-title">Co-Founder / Investor</p>
      <p class="contact-line contact-email">danavellor@mailbrook.example</p>
      <p class="contact-line contact-phone">805-555-0147</p>
      <p class="contact-line contact-web">www.hrseedcollective.example</p>
    </div>
  </article>
</main>
</body>
</html>
```